NEED LABEL FOR PACKAGED DRINKING WATER BOTTLE

we are a new company who is into manufacturing of packaged drinking water bottles in 200 ml 500 ml and 1000 ml. we already have a label which we are using in our local market but we are introducing our 200ml bottle in inflight catering where our products will be seen, consumed by various age and origin of people who travel on flights. so we want a label which is simple and elegant.the bottle is a square bottle and label size would be 198 mm x 36 mm.you can use the label provided below for reference.and the bottle shape also is provided
Target Market(s)
flight passengers in domestic flights
Industry/Entity Type
It Company
Look and feel

```html
<!DOCTYPE html>
<html lang="en">
<head>
<meta charset="utf-8">
<title>NIRVA Packaged Drinking Water – 200 ml Label</title>
<link href="https://fonts.googleapis.com/css2?family=Arimo:ital,wght@0,400;0,700;1,700&display=swap" rel="stylesheet">
<style>
  :root {
    --label-yellow: #fecb2e;
    --ink: #111111;
    --brand-blue: #3cc2f0;
    --tag-yellow: #f7f56a;
    --tag-blue: #1440d8;
    --frame-grey: #d6d6d6;
    --drops-light: #ffffff;
    --drops-mid: #eef1f4;
  }
  * { box-sizing: border-box; margin: 0; padding: 0; }
  html, body { width: 1200px; height: 438px; overflow: hidden; background: #ffffff; }
  body { font-family: "Arimo", Arial, sans-serif; color: var(--ink); }

  .label {
    position: relative;
    width: 1200px;
    height: 438px;
    border: 2px solid var(--frame-grey);
    overflow: hidden;
  }

  .droplet-backdrop {
    position: absolute;
    inset: 0;
    background:
      radial-gradient(circle at 30% 40%, var(--drops-mid) 0, transparent 55%),
      radial-gradient(circle at 80% 70%, var(--drops-mid) 0, transparent 50%),
      linear-gradient(180deg, var(--drops-light), #f6f7f9);
  }

  .info-panel {
    position: absolute;
    left: 26px; top: 29px;
    width: 473px; height: 384px;
    background: var(--label-yellow);
    padding: 28px 26px 0 28px;
  }

  .net-quantity { font-size: 28px; line-height: 1; }
  .net-quantity strong { font-weight: 700; }
  .net-quantity em { font-size: 19px; font-weight: 700; }

  .batch-block { position: relative; margin-top: 10px; height: 74px; }
  .batch-fields { list-style: none; font-size: 14.5px; line-height: 25px; width: 202px; }
  .batch-fields li { display: flex; justify-content: space-between; }
  .batch-brace { position: absolute; left: 206px; top: -6px; font-size: 66px; font-weight: 400; line-height: 1; transform: scaleX(0.7); }
  .batch-note { position: absolute; left: 246px; top: 24px; font-size: 17.5px; }

  .dotted-rule { border: 0; border-top: 2px dotted var(--ink); width: 306px; }
  .rule-top { margin-top: 12px; }

  .cert-block { position: relative; height: 78px; }
  .cert-text { font-size: 18px; line-height: 26px; padding-top: 12px; }
  .cert-mark { position: absolute; left: 320px; top: -14px; width: 100px; text-align: center; font-size: 10.5px; }
  .cert-badge { display: block; width: 60px; height: 50px; margin: 3px auto 3px; border: 4px solid var(--ink); border-radius: 4px; }

  .storage-note { font-size: 12.5px; line-height: 17px; margin-top: 16px; width: 420px; }

  .disposal-row { position: relative; margin-top: 10px; height: 90px; }
  .recycle-icon { position: absolute; left: 0; top: 6px; width: 52px; height: 52px; border-radius: 50%; background: var(--ink); }
  .recycle-caption { position: absolute; left: -6px; top: 68px; font-size: 12.5px; }
  .crush-text { position: absolute; left: 76px; top: 18px; font-size: 21px; }
  .bin-figure { position: absolute; left: 374px; top: 0; width: 62px; height: 62px; background: linear-gradient(180deg, #3a3a3a, #111); border-radius: 6px; }
  .bin-caption { position: absolute; left: 288px; top: 68px; font-size: 12.5px; }

  .brand-lockup {
    position: absolute;
    left: 574px; top: 140px;
    width: 520px;
    text-align: center;
  }
  .brand-name {
    font-size: 132px;
    font-weight: 700;
    line-height: 1;
    letter-spacing: 4px;
    color: var(--brand-blue);
  }

  .product-tag {
    position: absolute;
    left: 604px; top: 291px;
    width: 461px; height: 39px;
    background: var(--tag-yellow);
    border-radius: 20px;
    color: var(--tag-blue);
    font-size: 23.5px;
    font-weight: 700;
    text-align: center;
    line-height: 39px;
    letter-spacing: 0.2px;
  }
</style>
</head>
<body>
  <div class="label">
    <div class="droplet-backdrop" role="img" aria-label="Scattered water droplets on a white background"></div>

    <section class="info-panel">
      <p class="net-quantity">Net Quantity : <strong>200</strong><em>ml</em></p>

      <div class="batch-block">
        <ul class="batch-fields">
          <li><span>MFG. DATE</span><span>:</span></li>
          <li><span>BATCH NO.</span><span>:</span></li>
          <li><span>M.R.P. (incl. of all taxes</span><span>:</span></li>
        </ul>
        <span class="batch-brace">}</span>
        <span class="batch-note">See Neck/Bottle</span>
      </div>

      <hr class="dotted-rule rule-top">
      <div class="cert-block">
        <p class="cert-text">For NSC certification details<br>see website: www.nsc-cert.org.in</p>
        <div class="cert-mark">
          <span>IS: 14543</span>
          <span class="cert-badge" role="img" aria-label="Certification badge"></span>
          <span>CM/L-5281063</span>
        </div>
      </div>
      <hr class="dotted-rule">

      <p class="storage-note">Best before six months from manufacture store in cool and dry hygienic conditions. Do not buy if seal/cap is broken.</p>

      <div class="disposal-row">
        <span class="recycle-icon" role="img" aria-label="Recycling symbol"></span>
        <span class="recycle-caption">Recyclable</span>
        <span class="crush-text">Crush the bottle after use</span>
        <span class="bin-figure" role="img" aria-label="Figure dropping litter into a bin"></span>
        <span class="bin-caption">Keep your city clean</span>
      </div>
    </section>

    <div class="brand-lockup">
      <p class="brand-name">NIRVA</p>
    </div>
    <p class="product-tag">PACKAGED DRINKING WATER</p>
  </div>
</body>
</html>
```